African homeware retailer needs a web page design

We need a web page design for a new homeware and accessories store based in Johannesburg, South Africa. Our store carries modern African inspired items from designers that support social development and poverty alleviation initiatives. We have a particular preference for outfits that are centred on the empowerment of women.

Our business celebrates the skill, design and product of African craft and the work of designers looking to take that forward in a socially beneficial way (creating employment, developing skills, supporting local crafts people etc). We aim to carry items and inspirations from all over the African continent.

We would like to see a design that communicates African beauty and elegance without the typical tribal references that are made in reference to African craft or art.

We would like the web page to be stylish, uncomplicated, modern, captivating and appealing to the discerning customer. A similar value proposition is that of http://www.lanterwickhouse.example/.

This is an e-commerce website which must be attractive to both individual buyers and design professionals so the website needs to look professional.

Here are links to some websites we like:
http://www.corvellinteriors.example/
http://www.tmerrow.example/

Our logo is attached to the brief.

Target Market(s)

Our target market is female, age 20-50. However should not alienate the design conscious male customer therefore

Industry/Entity Type

E-Commerce

Requirements
Must have
• - A featured product banner which includes a photograph and text. This should be easy to edit as we will be changing the featured product regularly
- An easily expendable products section with categories. Examples of categories could be cushions, bedding, crockery etc. Should be easy to add new categories as well as new product pictures
- Home/landing page should be uncluttered
- Should use the logo and should be easy to change the logo which we have in various colour combinations. We plan to change the logo colours depending on circumstance e.g. make it red and white around Valentines day (similar to the way Quorbit frequently changes the logo on their landing page)

```html
<!DOCTYPE html>
<html lang="en">
<head>
<meta charset="utf-8">
<title>Kora Living – Home</title>
<link href="https://fonts.googleapis.com/css2?family=Open+Sans:wght@400;600;700&display=swap" rel="stylesheet">
<style>
:root{
  --orange:#e8541e;
  --orange-dark:#c9410f;
  --teal:#3f8f8c;
  --ink:#333;
  --muted:#888;
  --line:#ddd;
  --panel:#f2f2f2;
  --dark:#3a3a3a;
  --badge:#c8322a;
  --white:#fff;
}
*{box-sizing:border-box;margin:0;padding:0}
html,body{width:730px;height:1200px;overflow:hidden}
body{font-family:"Open Sans",Arial,sans-serif;color:var(--ink);background:#f7f7f7;font-size:9px;position:relative}

/* header */
.site-header{position:absolute;left:0;top:0;width:730px;height:106px;background:var(--white)}
.brand{position:absolute;left:62px;top:22px;display:flex;flex-direction:column;align-items:center;gap:6px}
.brand-mark{width:34px;height:34px;background:var(--orange)}
.brand-name{font-size:13px;font-weight:700;color:var(--teal);letter-spacing:1px;line-height:1}
.util-links{position:absolute;right:60px;top:8px;display:flex;gap:6px;font-size:7px;color:var(--ink)}
.util-links span{border:1px solid var(--line);padding:1px 5px}
.call-us{position:absolute;right:60px;top:34px;text-align:right;font-size:8px;color:var(--orange)}
.call-us strong{display:block;font-size:11px}

.main-nav{position:absolute;left:0;top:106px;width:730px;height:21px;background:var(--orange);display:flex;align-items:center;padding-left:60px}
.main-nav a{color:var(--white);font-size:8px;font-weight:600;padding:0 8px;line-height:21px}
.main-nav a.active{background:var(--orange-dark)}
.nav-search{margin-left:auto;margin-right:60px;width:70px;height:12px;background:var(--white);font-size:6px;color:var(--muted);padding:1px 4px}

/* sidebar */
.sidebar{position:absolute;left:60px;top:142px;width:130px;background:var(--white)}
.panel-title{background:var(--teal);color:var(--white);font-weight:700;font-size:8px;padding:7px 8px;text-transform:uppercase}
.cat-list{list-style:none;background:var(--panel);padding:7px 8px 8px}
.cat-list li{display:flex;align-items:center;font-size:7px;line-height:12.5px}
.cat-list li::before{content:"";width:7px;height:7px;border:1px solid #aaa;background:var(--white);margin-right:6px}
.cat-list li.sub{padding-left:14px}
.cat-list .count{margin-left:auto;background:var(--badge);color:var(--white);font-size:6px;padding:0 4px;line-height:8px}
.cat-list li.top{font-size:6px;text-transform:uppercase}
.cushions-title{margin-top:8px;padding:10px 8px}
.feature-photo{height:130px;background:linear-gradient(135deg,#d9462a,#2a6f8f 40%,#e5b52f 65%,#7a3f8c)}
.news{padding:12px 6px 4px}
.news h2{font-size:30px;font-weight:400;line-height:1}
.news .date{font-size:7px;margin-top:8px;font-weight:600}
.news .lead{font-size:7px;line-height:9px;margin-top:2px}
.news p{font-size:6px;color:var(--muted);line-height:8px;margin-top:6px}
.news-photo{height:62px;margin:8px 6px 0;background:linear-gradient(135deg,#b87a3a,#6b4a2a 50%,#d9b36a)}
.dots{display:flex;justify-content:center;gap:4px;margin:8px 0}
.dots i{width:4px;height:4px;border-radius:50%;background:#aaa}
.dots i:first-child{background:var(--ink)}
.social-box{background:var(--dark);height:40px;display:flex;justify-content:space-around;align-items:center}
.social-box span{width:16px;height:16px;border-radius:50%;border:1px solid var(--white)}

/* main */
.content{position:absolute;left:196px;top:142px;width:476px;height:806px;background:var(--white);box-shadow:0 0 4px rgba(0,0,0,.15)}
.toolbar{display:flex;align-items:center;height:20px;padding:0 8px 0 40px}
.toolbar .search{width:100px;height:11px;border:1px solid var(--line);font-size:5px;color:var(--muted);padding:1px 4px}
.view-icons{margin-left:auto;display:flex;gap:6px}
.hero{height:256px;background:radial-gradient(ellipse at 50% 55%,#d6d6d6,#9a9a9a 35%,#e2562a 48%,#5a5a5a 62%,#2d2d2d 85%)}
.hero-copy{text-align:center;font-size:16px;line-height:20px;padding:12px 30px 6px;color:#444}
.section-label{text-align:center;color:var(--orange);font-size:6px;text-transform:uppercase;margin:8px 0 4px}
.product-row{position:relative;display:flex;gap:6px;justify-content:center;border-top:1px solid var(--line);border-bottom:1px solid var(--line);padding:6px 0;background:#fafafa}
.product{width:96px;background:var(--white)}
.product .price{font-size:6px;padding:2px 4px;display:flex;justify-content:space-between}
.product .price::after{content:"";width:7px;height:6px;background:var(--orange)}
.product .photo{height:118px}
.bowl{background:radial-gradient(circle at 50% 60%,#e5b52f,#2a6f8f 35%,#c8322a 55%,#ececec 72%)}
.horse{background:radial-gradient(ellipse at 50% 55%,#3a3a3a,#8a8a8a 35%,#ececec 65%)}
.basket{background:radial-gradient(ellipse at 50% 55%,#2a6f8f,#8bb6a8 30%,#6b4a2a 45%,#ececec 65%)}
.boat{background:radial-gradient(ellipse at 50% 60%,#8a4a22,#b8743e 30%,#ececec 55%)}
.row-arrow{position:absolute;top:50%;width:12px;height:12px;border-radius:50%;background:var(--ink);margin-top:-6px}
.row-arrow.prev{left:6px}.row-arrow.next{right:6px}
.pager{position:absolute;left:0;right:0;bottom:20px;display:flex;justify-content:center;gap:2px}
.pager span{width:12px;height:12px;border:1px solid var(--line);font-size:6px;text-align:center;line-height:10px;background:var(--white)}
.pager span.current{background:var(--orange);color:var(--white);border-color:var(--orange)}

/* categories strip */
.categories{position:absolute;left:0;top:956px;width:730px;text-align:center}
.categories h3{color:var(--orange);font-size:11px;text-transform:uppercase;letter-spacing:1px}
.cat-buttons{display:flex;justify-content:center;align-items:center;gap:10px;margin-top:8px}
.cat-buttons span.btn{width:150px;height:20px;border:1px solid var(--line);background:var(--panel);font-size:10px;line-height:18px}
.chev{font-size:12px;color:var(--muted)}

/* footer */
.site-footer{position:absolute;left:0;top:1018px;width:730px;height:182px;background:var(--white);border-top:1px solid var(--line)}
.footer-brand{position:absolute;left:66px;top:30px;display:flex;flex-direction:column;align-items:center;gap:6px}
.footer-brand .brand-mark{width:40px;height:40px}
.footer-brand .brand-name{font-size:15px}
.footer-col{position:absolute;top:16px}
.footer-col h4{font-size:7px;font-weight:700;text-transform:uppercase;margin-bottom:5px}
.footer-col li{list-style:none;font-size:6.5px;line-height:10px;color:#555}
.links{left:218px}
.contact{left:360px}
.contact .field{width:110px;height:11px;background:var(--white);border:1px solid var(--line);font-size:6px;color:var(--muted);padding:0 3px;margin-bottom:3px}
.contact .field.msg{height:34px}
.contact .submit{width:40px;height:12px;background:var(--orange);color:var(--white);font-size:6px;text-align:center;line-height:12px;margin-top:6px}
.follow{left:548px;width:130px;text-align:center}
.icons{display:flex;justify-content:center;gap:4px;margin-bottom:8px}
.icons span{width:14px;height:14px;background:var(--orange)}
.cards{display:flex;justify-content:center;gap:4px;margin-bottom:4px}
.cards span{width:20px;height:12px;background:#b9c4d0}
.copyright{font-size:5.5px;color:var(--muted);margin-top:4px}
</style>
</head>
<body>

<header class="site-header">
  <div class="brand"><span class="brand-mark"></span><span class="brand-name">KORA LIVING</span></div>
  <div class="util-links"><span>Order Status | Help</span><span>LOGIN | SIGN UP</span></div>
  <div class="call-us">Call us<strong>555-014-2290</strong></div>
</header>

<nav class="main-nav">
  <a class="active">Shop Now</a><a>Our Story</a><a>Blog</a><a>Custom Design</a><a>Our Shop</a><a>Press &amp; Mentions</a><a>Designer &amp; Architects</a><a>Video</a><a>Contact</a>
  <div class="nav-search">Search...</div>
</nav>

<aside class="sidebar">
  <div class="panel-title">All Categories</div>
  <ul class="cat-list">
    <li>All Items<span class="count">24</span></li>
    <li class="sub">Bedding<span class="count">6</span></li>
    <li class="sub">Wall<span class="count">3</span></li>
    <li class="sub">Decor<span class="count">8</span></li>
    <li class="sub">Stools<span class="count">4</span></li>
    <li class="sub">Chairs<span class="count">5</span></li>
    <li class="sub">Cushions<span class="count">9</span></li>
    <li class="sub">Lamps<span class="count">2</span></li>
    <li class="sub">Bowls &amp; Trays<span class="count">7</span></li>
    <li class="sub">Dining Chairs<span class="count">3</span></li>
    <li class="sub">Dining Tables<span class="count">2</span></li>
    <li class="top">Baskets</li>
    <li class="top">Rugs</li>
    <li class="top">Table Linen</li>
    <li class="top">Lamp Shades</li>
    <li class="top">Mirrors</li>
    <li class="top">Throws</li>
  </ul>
  <div class="panel-title cushions-title">Cushions of the Week</div>
  <div class="feature-photo" role="img" aria-label="Stack of brightly patterned cushions"></div>
  <div class="news">
    <h2>NEWS</h2>
    <div class="date">18th March 2014</div>
    <div class="lead">New woven bowl range, from our makers.</div>
    <p>Local artisans share the story behind each handmade piece in store now.</p>
    <p>Visit our showroom for the new season launch and meet the designers.</p>
  </div>
  <div class="news-photo" role="img" aria-label="Handmade wooden bowls"></div>
  <div class="dots"><i></i><i></i><i></i><i></i><i></i></div>
  <div class="social-box"><span></span><span></span><span></span></div>
</aside>

<main class="content">
  <div class="toolbar">
    <div class="search">Search Products</div>
    <div class="view-icons">
      <svg width="9" height="9" viewBox="0 0 10 10"><path d="M0 1h10M0 5h10M0 9h10" stroke="#333" stroke-width="1.6"/></svg>
      <svg width="9" height="9" viewBox="0 0 10 10"><path d="M0 0h4v4H0zM6 0h4v4H6zM0 6h4v4H0zM6 6h4v4H6z" fill="#333"/></svg>
    </div>
  </div>
  <div class="hero" role="img" aria-label="Featured product: beaded wire motorbike sculpture"></div>
  <p class="hero-copy">Lorem ipsum dolor sit amet, consectetuer adipiscing elit, sed diam nonu nibh euismod tincidunt ut laoreet dolore magna aliquam erat volutpat.</p>
  <div class="section-label">Featured Products</div>
  <div class="product-row">
    <span class="row-arrow prev"></span>
    <div class="product"><div class="price">$ 144.00</div><div class="photo bowl" role="img" aria-label="Woven bowl"></div></div>
    <div class="product"><div class="price">$ 120.00</div><div class="photo horse" role="img" aria-label="Beaded wire horse figure"></div></div>
    <div class="product"><div class="price">$ 150.00</div><div class="photo basket" role="img" aria-label="Striped woven basket"></div></div>
    <div class="product"><div class="price">$ 120.00</div><div class="photo boat" role="img" aria-label="Carved wooden boat bowl"></div></div>
    <span class="row-arrow next"></span>
  </div>
  <div class="section-label">New Products</div>
  <div class="product-row">
    <span class="row-arrow prev"></span>
    <div class="product"><div class="price">$ 144.00</div><div class="photo bowl" role="img" aria-label="Stacked woven bowls"></div></div>
    <div class="product"><div class="price">$ 120.00</div><div class="photo horse" role="img" aria-label="Beaded wire horse figure"></div></div>
    <div class="product"><div class="price">$ 150.00</div><div class="photo basket" role="img" aria-label="Striped woven basket"></div></div>
    <div class="product"><div class="price">$ 120.00</div><div class="photo boat" role="img" aria-label="Carved wooden boat bowl"></div></div>
    <span class="row-arrow next"></span>
  </div>
  <div class="pager"><span>‹</span><span class="current">1</span><span>2</span><span>3</span><span>4</span><span>›</span></div>
</main>

<section class="categories">
  <h3>Categories</h3>
  <div class="cat-buttons">
    <span class="chev">‹</span>
    <span class="btn">Cushions</span><span class="btn">Bedding</span><span class="btn">Crockery</span>
    <span class="chev">›</span>
  </div>
</section>

<footer class="site-footer">
  <div class="footer-brand"><span class="brand-mark"></span><span class="brand-name">KORA LIVING</span></div>
  <div class="footer-col links">
    <h4>Quick Links</h4>
    <ul><li>Shop Now</li><li>Our Story</li><li>Blog</li><li>Custom Design</li><li>Our Shop</li><li>Press &amp; Mentions</li><li>Designer &amp; Architects</li><li>Video</li><li>Contact</li></ul>
  </div>
  <div class="footer-col contact">
    <h4>Quick Contact</h4>
    <div class="field">Name</div><div class="field">Phone</div><div class="field">Email</div><div class="field msg">Message</div>
    <div class="submit">Submit</div>
  </div>
  <div class="footer-col follow">
    <h4>Follow Us</h4>
    <div class="icons"><span></span><span></span><span></span><span></span></div>
    <div class="cards"><span></span><span></span><span></span></div>
    <div class="cards"><span></span><span></span><span></span></div>
    <div class="copyright">© 2014 KoraLiving. All Rights Reserved</div>
  </div>
</footer>

</body>
</html>
```